Sorlen cards

I want a simple business card that pops.
Logo on one side.
On side two i want.
"Are you thinking about a new building on your property, or renovating an existing structure? Contact".....
Owners Name: Dale Whitcombe
Owners Phone number: 717-555-0192
Address:4716 Oxtail Ridge RD, Carvell, PA 15547
Committed to Quality, Service, and Integrity

```html
<!DOCTYPE html>
<html lang="en">
<head>
<meta charset="utf-8">
<title>Sorlen Builders LLC – Business Card</title>
<link rel="stylesheet" href="https://fonts.googleapis.com/css2?family=Arimo:wght@400;700&family=Kalam:wght@400&display=swap">
<style>
  :root {
    --stage: #2a2a2a;
    --brown-light: #a08a6e;
    --brown-mid: #7a6049;
    --brown-dark: #4e3525;
    --ink: #3b2a1e;
    --tan: #9a8266;
    --paper: #f2f1ef;
    --paper-edge: #e4e3e0;
    --cream: #f4efe8;
    --rule: #c9b9a5;
  }
  * { box-sizing: border-box; margin: 0; padding: 0; }
  html, body {
    width: 1200px; height: 576px; overflow: hidden;
    background: var(--stage);
    font-family: "Arimo", Arial, sans-serif;
  }
  .sheet { position: relative; width: 1200px; height: 576px; }

  .card {
    position: absolute; top: 139px;
    height: 292px;
    border-radius: 10px; overflow: hidden;
  }

  /* Front side */
  .card--front {
    left: 102px; width: 484px;
    background: linear-gradient(180deg, var(--brown-light) 0%, var(--brown-mid) 50%, var(--brown-dark) 100%);
    color: var(--cream);
  }
  .front-brand {
    position: absolute; left: 0; right: 0; top: 51px;
    display: flex; flex-direction: column; align-items: center;
  }
  .front-brand__mark {
    width: 96px; height: 96px;
    background: rgba(244, 239, 232, 0.3);
    margin-bottom: 10px;
  }
  .front-brand__name {
    font-weight: 700; font-size: 52px; line-height: 1; letter-spacing: 1px;
    color: var(--cream);
  }
  .front-brand__sub {
    font-weight: 700; font-size: 17px; letter-spacing: 2px; line-height: 1;
    margin-top: 6px; color: var(--cream);
  }
  .front-tagline {
    position: absolute; left: 0; right: 0; top: 255px;
    display: flex; align-items: center; justify-content: center; gap: 10px;
    font-size: 13px; color: var(--cream);
  }
  .front-tagline__rule {
    width: 68px; height: 1px;
    background: linear-gradient(90deg, rgba(244,239,232,0), rgba(244,239,232,0.9));
  }
  .front-tagline__rule--right {
    background: linear-gradient(90deg, rgba(244,239,232,0.9), rgba(244,239,232,0));
  }

  /* Back side */
  .card--back {
    left: 596px; width: 480px; top: 138px; height: 291px;
    background: linear-gradient(135deg, var(--paper) 0%, var(--paper-edge) 100%);
  }
  .back-brand {
    position: absolute; top: 24px; left: 0; right: 0;
    display: flex; justify-content: center; align-items: center; gap: 20px;
  }
  .back-brand__mark { width: 60px; height: 60px; background: var(--ink); }
  .back-brand__text { display: flex; flex-direction: column; align-items: center; }
  .back-brand__name {
    font-weight: 700; font-size: 40px; line-height: 1; letter-spacing: 1px; color: var(--ink);
  }
  .back-brand__sub {
    font-weight: 700; font-size: 13px; letter-spacing: 3px; line-height: 1;
    margin-top: 3px; color: var(--ink);
  }
  .back-pitch {
    position: absolute; top: 102px; left: 0; right: 0;
    text-align: center;
    font-family: "Kalam", "Comic Sans MS", cursive;
    font-size: 17px; line-height: 22px; color: var(--ink);
  }
  .back-contact-label {
    position: absolute; top: 157px; left: 46px; right: 46px;
    display: flex; align-items: center; gap: 10px;
    font-size: 9px; color: var(--ink);
  }
  .back-contact-label::before,
  .back-contact-label::after { content: ""; flex: 1; height: 1px; background: var(--rule); }
  .back-person {
    position: absolute; top: 176px; left: 0; right: 0; text-align: center;
    font-weight: 700; font-size: 20px; color: var(--ink);
  }
  .back-person__last { color: var(--tan); }
  .back-phone {
    position: absolute; top: 205px; left: 0; right: 0; text-align: center;
    font-weight: 700; font-size: 14px; color: var(--ink);
  }
  .back-address {
    position: absolute; top: 225px; left: 0; right: 0; text-align: center;
    font-size: 13px; color: var(--tan);
  }
  .back-band {
    position: absolute; left: 0; right: 0; bottom: 0; height: 30px;
    background: linear-gradient(180deg, var(--brown-mid), var(--brown-dark));
    display: flex; align-items: center; justify-content: center;
    font-size: 13px; color: var(--cream);
  }
</style>
</head>
<body>
<main class="sheet">
  <section class="card card--front" aria-label="Card front">
    <div class="front-brand">
      <span class="front-brand__mark" aria-hidden="true"></span>
      <span class="front-brand__name">SORLEN</span>
      <span class="front-brand__sub">BUILDERS LLC</span>
    </div>
    <p class="front-tagline">
      <span class="front-tagline__rule"></span>
      Committed to Quality, Service &amp; Integrity
      <span class="front-tagline__rule front-tagline__rule--right"></span>
    </p>
  </section>

  <section class="card card--back" aria-label="Card back">
    <div class="back-brand">
      <span class="back-brand__mark" aria-hidden="true"></span>
      <div class="back-brand__text">
        <span class="back-brand__name">SORLEN</span>
        <span class="back-brand__sub">BUILDERS LLC</span>
      </div>
    </div>
    <p class="back-pitch">Are you thinking about a new building on your<br>property, or renovating an existing structure?</p>
    <p class="back-contact-label">Contact:</p>
    <p class="back-person">DALE <span class="back-person__last">WHITCOMBE</span></p>
    <p class="back-phone">Call: 717-555-0192</p>
    <p class="back-address">Add.: 4716 Oxtail Ridge RD, Carvell, PA 15547</p>
    <p class="back-band">Committed to Quality, Service &amp; Integrity</p>
  </section>
</main>
</body>
</html>
```